QuorvelLabsCrew PowerPoint and Word document templates

We need a design for a powerpoint template, which will be used at various conferences to deliver sessions about topics like Machine Learning, Data Science, Big Data and database technologies. The deck should include several types of layouts, a nice landing page with graphics resembling the topic, oneline title with contect and some slide for section separation. Additionally we would like to request a word document template, which would match the PowerPoint graphics and styles - entry pages with nice images, headline styles, footer with logo which is a part of the design project as a followup.

Target Market(s)

computer science professionals, attendees of conferences with database, AI, machine learning and big data topics

Logo Text

QuorvelLabsCrew

Font styles to use
Sans Serif

Colors

Designer to choose colors to be used in the design.

```html
<!DOCTYPE html>
<html lang="en">
<head>
<meta charset="utf-8">
<title>QuorvelLabsCrew – Presentation Template</title>
<link rel="stylesheet" href="https://fonts.googleapis.com/css2?family=Arimo:wght@400;700&family=Open+Sans:wght@400;600&family=Oswald:wght@500;600&display=swap">
<style>
  :root{
    --blue:#3a78c0;
    --blue-dark:#2a62a8;
    --blue-soft:#7fa6d6;
    --blue-pale:#b7cfee;
    --ink:#151515;
    --paper:#f4f5f7;
    --stage:#c4c4c4;
    --label:#3c3c3c;
  }
  html,body{margin:0;padding:0;width:1200px;height:787px;overflow:hidden;background:var(--stage);}
  .board{position:absolute;left:0;top:0;width:1500px;height:984px;transform:scale(.8);transform-origin:0 0;}
  .slide{position:absolute;width:692px;height:389px;background:var(--paper);box-shadow:0 2px 6px rgba(0,0,0,.25);overflow:hidden;font-family:"Open Sans",sans-serif;color:var(--ink);}
  .slide-cover{left:33px;top:44px}
  .slide-p1{left:773px;top:44px}
  .slide-p2{left:33px;top:512px}
  .slide-p3{left:773px;top:512px}
  .caption{position:absolute;width:692px;text-align:center;font-family:"Open Sans",sans-serif;font-size:29px;color:var(--label);letter-spacing:.5px;}
  .frame{position:absolute;left:0;top:0;width:692px;height:389px;}
  .footer-url{position:absolute;left:0;right:0;top:366px;text-align:center;font-family:"Arimo",sans-serif;font-size:8.5px;letter-spacing:2px;color:#fff;}
  .footer-url::before,.footer-url::after{content:"";display:inline-block;width:70px;height:1px;background:#fff;vertical-align:middle;margin:0 8px;}
  .page-no{position:absolute;right:28px;top:368px;font-family:"Arimo",sans-serif;font-size:8px;font-weight:700;color:var(--ink);}
  .heading{position:absolute;left:20px;top:26px;margin:0;font-family:"Arimo",sans-serif;font-weight:700;font-size:21px;padding-bottom:2px;border-bottom:2px solid var(--blue);}
  .heading span{color:var(--blue-soft)}
  .body-copy{position:absolute;left:21px;width:650px;font-size:8.4px;line-height:12px;margin:0;}
  .body-copy p{margin:0 0 11px}
  .photo{position:absolute}
  /* cover */
  .logo-box{position:absolute;left:25px;top:22px;height:45px;padding:0 10px;border:1.5px solid var(--blue-dark);display:flex;align-items:center;font-family:"Arimo",sans-serif;font-size:25px;color:var(--blue-dark);}
  .title-main{position:absolute;right:22px;top:82px;margin:0;text-align:right;font-family:"Oswald",sans-serif;font-weight:600;line-height:45px;font-size:40px;}
  .title-main .accent{color:var(--blue);display:block}
  .title-main .plain{color:var(--ink);display:block}
  .cover-blurb{position:absolute;left:442px;top:216px;width:227px;color:#fff;font-family:"Arimo",sans-serif;font-size:8.6px;line-height:11.2px;text-align:justify;margin:0;}
  .cover-tagline{position:absolute;left:51px;top:303px;margin:0;font-family:"Arimo",sans-serif;font-weight:700;font-size:35px;letter-spacing:.3px;}
  /* page 01 cards */
  .card{position:absolute;top:170px;width:139px}
  .card-icon{height:36px;background:var(--blue);display:flex;align-items:center;justify-content:center;}
  .card-title{margin:10px 0 6px;text-align:center;font-family:"Arimo",sans-serif;font-weight:700;font-size:10.5px;}
  .card-text{height:92px;box-sizing:border-box;padding:12px 14px;background:var(--blue);color:#fff;font-size:7.6px;line-height:11.2px;text-align:justify;margin:0;}
  /* page 02 */
  .strip-panel{position:absolute;top:71px;width:137px;height:163px;background:var(--blue);box-sizing:border-box;padding:26px 13px 0;color:#fff;}
  .strip-panel svg{display:block;margin:0 auto 18px}
  .strip-panel p{margin:0;font-size:7.6px;line-height:11.2px;text-align:justify}
  /* page 03 */
  .topic-bar{position:absolute;left:163px;width:123px;height:30px;background:var(--blue-soft);color:#fff;font-family:"Arimo",sans-serif;font-weight:700;font-size:10.5px;display:flex;align-items:center;justify-content:center;}
  .topic-text{position:absolute;left:311px;width:362px;margin:0;font-size:7.9px;line-height:12px}
</style>
</head>
<body>
<div class="board">

  <!-- Cover -->
  <section class="slide slide-cover">
    <svg class="frame" viewBox="0 0 692 389" aria-hidden="true">
      <polygon points="0,91 400,91 425,116 0,116" fill="var(--blue-pale)"/>
      <polygon points="397,91 455,91 560,202 505,202" fill="var(--blue-pale)"/>
      <polygon points="350,91 395,91 470,202 425,202" fill="var(--blue-soft)"/>
      <polygon points="420,202 692,202 692,284 400,284" fill="var(--blue)"/>
    </svg>
    <div class="photo" role="img" aria-label="Businessman using a tablet with glowing network technology diagram" style="left:0;top:117px;width:440px;height:167px;clip-path:polygon(0 0,345px 0,428px 83px,345px 167px,0 167px);background:radial-gradient(circle at 62% 45%,#3fa8ec 0%,#1463b8 35%,#0a2a6a 75%,#0a1c45 100%);"></div>
    <svg class="frame" viewBox="0 0 692 389" aria-hidden="true">
      <polygon points="345,117 370,117 455,200 370,284 345,284 428,200" fill="#fff"/>
    </svg>
    <div class="logo-box">QuorvelLabsCrew</div>
    <h1 class="title-main"><span class="accent">PRESENTATION</span><span class="plain">TITLE HERE</span></h1>
    <p class="cover-blurb">Lorem Ipsum is simply dummy text of the printing and typesetting industry. Lorem Ipsum has been the industry's standard dummy text ever since the 1500s, when an unknown printer took a galley of type and scrambled it to make a type specimen book.</p>
    <h2 class="cover-tagline">LOREM IPSUM IS SIMPLY DUMMY</h2>
    <svg class="frame" viewBox="0 0 692 389" aria-hidden="true">
      <polygon points="282,0 692,0 692,17 298,17" fill="var(--blue)"/>
      <line x1="236" y1="0" x2="256" y2="17" stroke="var(--blue-soft)" stroke-width="3"/>
      <line x1="250" y1="0" x2="280" y2="30" stroke="var(--blue)" stroke-width="3"/>
      <polygon points="55,358 638,358 662,389 80,389" fill="var(--blue)"/>
      <line x1="643" y1="358" x2="672" y2="389" stroke="var(--blue)" stroke-width="4"/>
      <line x1="660" y1="356" x2="690" y2="389" stroke="var(--blue)" stroke-width="3"/>
      <line x1="0" y1="342" x2="45" y2="389" stroke="var(--blue)" stroke-width="4"/>
      <line x1="0" y1="358" x2="30" y2="389" stroke="var(--blue)" stroke-width="4"/>
      <polygon points="0,374 0,389 14,389" fill="var(--blue)"/>
    </svg>
    <div class="footer-url">www.quorvellabs.com</div>
  </section>

  <!-- Page 01 -->
  <section class="slide slide-p1">
    <h2 class="heading">LOREM <span>IPSUM</span></h2>
    <div class="body-copy" style="top:68px">
      <p>Lorem Ipsum is simply dummy text of the printing and typesetting industry. Lorem Ipsum has been the industry's standard dummy text ever since the 1500s, when an unknown printer took a galley of type and scrambled it to make a type specimen book.</p>
      <p>It has survived not only five centuries, but also the leap into electronic typesetting, remaining essentially unchanged. It was popularised in the 1960s with the release of Lettrex sheets containing Lorem Ipsum passages, and more recently with desktop publishing software like Paginor Desk including versions of Lorem Ipsum.</p>
    </div>
    <div class="card" style="left:21px">
      <div class="card-icon"><svg width="22" height="22" viewBox="0 0 22 22"><circle cx="11" cy="7" r="4" fill="#fff"/><path d="M3 21v-3c0-3 3-5 8-5s8 2 8 5v3z" fill="#fff"/></svg></div>
      <h3 class="card-title">LOREM IPSUM</h3>
      <p class="card-text">Lorem Ipsum is simply dummy text of the printing and typesetting industry. Lorem Ipsum has been the industry's standard dummy text ever since the 1500s.</p>
    </div>
    <div class="card" style="left:192px">
      <div class="card-icon"><svg width="22" height="22" viewBox="0 0 22 22" fill="none" stroke="#fff" stroke-width="2.4"><rect x="2" y="9" width="11" height="6" rx="3" transform="rotate(-45 7.5 12)"/><rect x="9" y="7" width="11" height="6" rx="3" transform="rotate(-45 14.5 10)"/></svg></div>
      <h3 class="card-title">LOREM IPSUM</h3>
      <p class="card-text">Lorem Ipsum is simply dummy text of the printing and typesetting industry. Lorem Ipsum has been the industry's standard dummy text ever since the 1500s.</p>
    </div>
    <div class="card" style="left:362px">
      <div class="card-icon"><svg width="22" height="22" viewBox="0 0 22 22" fill="none" stroke="#fff" stroke-width="2.4"><circle cx="9" cy="9" r="6"/><line x1="13.5" y1="13.5" x2="20" y2="20" stroke-width="3.2"/></svg></div>
      <h3 class="card-title">LOREM IPSUM</h3>
      <p class="card-text">Lorem Ipsum is simply dummy text of the printing and typesetting industry. Lorem Ipsum has been the industry's standard dummy text ever since the 1500s.</p>
    </div>
    <div class="card" style="left:531px">
      <div class="card-icon"><svg width="22" height="22" viewBox="0 0 22 22" fill="none" stroke="#fff" stroke-width="1.8"><rect x="4" y="2" width="14" height="18" rx="1"/><circle cx="11" cy="9" r="3"/><line x1="7" y1="16" x2="15" y2="16"/></svg></div>
      <h3 class="card-title">LOREM IPSUM</h3>
      <p class="card-text">Lorem Ipsum is simply dummy text of the printing and typesetting industry. Lorem Ipsum has been the industry's standard dummy text ever since the 1500s.</p>
    </div>
    <svg class="frame" viewBox="0 0 692 389" aria-hidden="true">
      <polygon points="282,0 692,0 692,17 298,17" fill="var(--blue)"/>
      <line x1="236" y1="0" x2="256" y2="17" stroke="var(--blue-soft)" stroke-width="3"/>
      <line x1="250" y1="0" x2="280" y2="30" stroke="var(--blue)" stroke-width="3"/>
      <polygon points="30,358 610,358 635,389 55,389" fill="var(--blue)"/>
      <line x1="612" y1="358" x2="642" y2="389" stroke="var(--blue)" stroke-width="4"/>
      <line x1="0" y1="342" x2="45" y2="389" stroke="var(--blue)" stroke-width="4"/>
      <line x1="0" y1="358" x2="30" y2="389" stroke="var(--blue)" stroke-width="4"/>
      <polygon points="0,374 0,389 14,389" fill="var(--blue)"/>
    </svg>
    <div class="footer-url">www.quorvellabs.com</div>
    <div class="page-no">01</div>
  </section>

  <!-- Page 02 -->
  <section class="slide slide-p2">
    <h2 class="heading">LOREM <span>IPSUM</span></h2>
    <div class="photo" role="img" aria-label="Office scenes: people at a desk with papers, laptop and newspaper" style="left:0;top:71px;width:692px;height:163px;background:linear-gradient(90deg,#6f6a66 0%,#3b3430 25%,#8a6a4a 45%,#5b5550 60%,#9a9a98 80%,#d8d8d6 100%);"></div>
    <div class="strip-panel" style="left:49px">
      <svg width="18" height="22" viewBox="0 0 22 22"><circle cx="11" cy="7" r="4" fill="#fff"/><path d="M3 21v-3c0-3 3-5 8-5s8 2 8 5v3z" fill="#fff"/></svg>
      <p>Lorem Ipsum is simply dummy text of the printing and typesetting industry. Lorem Ipsum has been the industry's standard dummy text ever since the 1500s.</p>
    </div>
    <div class="strip-panel" style="left:275px">
      <svg width="22" height="22" viewBox="0 0 22 22" fill="none" stroke="#fff" stroke-width="2.4"><rect x="2" y="9" width="11" height="6" rx="3" transform="rotate(-45 7.5 12)"/><rect x="9" y="7" width="11" height="6" rx="3" transform="rotate(-45 14.5 10)"/></svg>
      <p>Lorem Ipsum is simply dummy text of the printing and typesetting industry. Lorem Ipsum has been the industry's standard dummy text ever since the 1500s.</p>
    </div>
    <div class="strip-panel" style="left:502px">
      <svg width="18" height="22" viewBox="0 0 18 22" fill="#fff"><circle cx="9" cy="8" r="6"/><rect x="6" y="14" width="6" height="4"/><rect x="6.5" y="19" width="5" height="2"/></svg>
      <p>Lorem Ipsum is simply dummy text of the printing and typesetting industry. Lorem Ipsum has been the industry's standard dummy text ever since the 1500s.</p>
    </div>
    <div class="body-copy" style="top:263px">
      <p>Lorem Ipsum is simply dummy text of the printing and typesetting industry. Lorem Ipsum has been the industry's standard dummy text ever since the 1500s, when an unknown printer took a galley of type and scrambled it to make a type specimen book.</p>
      <p>It has survived not only five centuries, but also the leap into electronic typesetting, remaining essentially unchanged. It was popularised in the 1960s with the release of Lettrex sheets containing Lorem Ipsum passages, and more recently with desktop publishing software like Paginor Desk including versions of Lorem Ipsum.</p>
    </div>
    <svg class="frame" viewBox="0 0 692 389" aria-hidden="true">
      <polygon points="282,0 692,0 692,17 298,17" fill="var(--blue)"/>
      <line x1="236" y1="0" x2="256" y2="17" stroke="var(--blue-soft)" stroke-width="3"/>
      <line x1="250" y1="0" x2="280" y2="30" stroke="var(--blue)" stroke-width="3"/>
      <polygon points="30,358 610,358 635,389 55,389" fill="var(--blue)"/>
      <line x1="612" y1="358" x2="642" y2="389" stroke="var(--blue)" stroke-width="4"/>
      <line x1="0" y1="342" x2="45" y2="389" stroke="var(--blue)" stroke-width="4"/>
      <line x1="0" y1="358" x2="30" y2="389" stroke="var(--blue)" stroke-width="4"/>
      <polygon points="0,374 0,389 14,389" fill="var(--blue)"/>
    </svg>
    <div class="footer-url">www.quorvellabs.com</div>
    <div class="page-no">02</div>
  </section>

  <!-- Page 03 -->
  <section class="slide slide-p3">
    <h2 class="heading">LOREM <span>IPSUM</span></h2>
    <svg class="frame" viewBox="0 0 692 389" aria-hidden="true">
      <path d="M85 82 H286 V111 H140 A62 62 0 0 0 85 82 Z" fill="var(--blue-soft)"/>
      <path d="M85 225 A72 72 0 0 0 140 201 H286 V231 H85 Z" fill="var(--blue-soft)"/>
      <circle cx="85" cy="153" r="72" fill="none" stroke="var(--blue-pale)" stroke-width="9"/>
    </svg>
    <div class="photo" role="img" aria-label="Glowing data globe above computer monitors in a city at night" style="left:20px;top:88px;width:130px;height:130px;border-radius:50%;background:radial-gradient(circle at 50% 40%,#4aa0ff 0%,#1a4fd0 45%,#0a1f70 80%,#061244 100%);"></div>
    <div class="topic-bar" style="top:82px">LOREM IPSUM</div>
    <div class="topic-bar" style="top:142px">LOREM IPSUM</div>
    <div class="topic-bar" style="top:201px">LOREM IPSUM</div>
    <p class="topic-text" style="top:87px">Lorem Ipsum is simply dummy text of the printing and typesetting industry. Lorem Ipsum has been the industry's standard dummy text ever since the 1500s.</p>
    <p class="topic-text" style="top:146px">Lorem Ipsum is simply dummy text of the printing and typesetting industry. Lorem Ipsum has been the industry's standard dummy text ever since the 1500s.</p>
    <p class="topic-text" style="top:205px">Lorem Ipsum is simply dummy text of the printing and typesetting industry. Lorem Ipsum has been the industry's standard dummy text ever since the 1500s.</p>
    <div class="body-copy" style="top:263px">
      <p>Lorem Ipsum is simply dummy text of the printing and typesetting industry. Lorem Ipsum has been the industry's standard dummy text ever since the 1500s, when an unknown printer took a galley of type and scrambled it to make a type specimen book.</p>
      <p>It has survived not only five centuries, but also the leap into electronic typesetting, remaining essentially unchanged. It was popularised in the 1960s with the release of Lettrex sheets containing Lorem Ipsum passages, and more recently with desktop publishing software like Paginor Desk including versions of Lorem Ipsum.</p>
    </div>
    <svg class="frame" viewBox="0 0 692 389" aria-hidden="true">
      <polygon points="282,0 692,0 692,17 298,17" fill="var(--blue)"/>
      <line x1="236" y1="0" x2="256" y2="17" stroke="var(--blue-soft)" stroke-width="3"/>
      <line x1="250" y1="0" x2="280" y2="30" stroke="var(--blue)" stroke-width="3"/>
      <polygon points="30,358 610,358 635,389 55,389" fill="var(--blue)"/>
      <line x1="612" y1="358" x2="642" y2="389" stroke="var(--blue)" stroke-width="4"/>
      <line x1="0" y1="342" x2="45" y2="389" stroke="var(--blue)" stroke-width="4"/>
      <line x1="0" y1="358" x2="30" y2="389" stroke="var(--blue)" stroke-width="4"/>
      <polygon points="0,374 0,389 14,389" fill="var(--blue)"/>
    </svg>
    <div class="footer-url">www.quorvellabs.com</div>
    <div class="page-no">03</div>
  </section>

  <div class="caption" style="left:33px;top:444px">COVER PAGE</div>
  <div class="caption" style="left:773px;top:444px">PAGE - 01</div>
  <div class="caption" style="left:33px;top:914px">PAGE - 02</div>
  <div class="caption" style="left:773px;top:914px">PAGE - 03</div>
</div>
</body>
</html>
```